Business Card Design Project

This is the first time we use our new logo. We need a business card that we can use both on our institutional corporate relationships and also that works for our staff that deals with consumers directly.

VELUNDA is a new company dedicated to empower consumers and to provide them with the best choices for specialized health care using the latest telemedicine technology (medicine at a distance via videoconference).

We want to print this cards in high quality materials and process. We will like designs that allow us to use UV spot varnish and other techniques that will differentiate us.

We are including Two different versions of Color logos. In addition we are including white over black background logos. Those can be used replacing the black for a color.

Please note this is the first time we will be creating any corporate materials with our new logo and colors.

Target Market(s)

34+ consumers of medium high and high socioeconomic levels.

Industry/Entity Type

Health

Requirements
Must have
• Our logo on its original colors
Should not have
• Any other graphical element or design that is not our logo

```html
<!DOCTYPE html>
<html lang="en">
<head>
<meta charset="utf-8">
<title>VELUNDA – Business Card</title>
<link rel="stylesheet" href="https://fonts.googleapis.com/css2?family=Source+Sans+3:ital,wght@0,400;0,600;1,400&display=swap">
<style>
  :root {
    --card-bg: #ffffff;
    --brand-blue: #1b4f9b;
    --accent-cyan: #62d4ea;
    --name-grey: #4f5759;
    --info-grey: #9aa2a5;
    --divider: #dde1e3;
  }
  * { margin: 0; padding: 0; box-sizing: border-box; }
  html, body {
    width: 1200px;
    height: 706px;
    overflow: hidden;
    background: var(--card-bg);
  }
  .card {
    position: relative;
    width: 1200px;
    height: 706px;
    background: var(--card-bg);
    font-family: "Source Sans 3", "Segoe UI", sans-serif;
    overflow: hidden;
  }
  .brand {
    position: absolute;
    left: 90px;
    top: 240px;
    width: 324px;
    text-align: center;
  }
  .brand-dot {
    display: block;
    margin: 0 auto 66px;
  }
  .brand-name {
    font-weight: 600;
    font-size: 64px;
    line-height: 1;
    letter-spacing: 3px;
    color: var(--brand-blue);
  }
  .divider {
    position: absolute;
    left: 506px;
    top: 144px;
    width: 2px;
    height: 432px;
    background: var(--divider);
  }
  .contact {
    position: absolute;
    left: 580px;
    top: 174px;
  }
  .person-name {
    font-size: 41px;
    font-weight: 400;
    line-height: 48px;
    color: var(--name-grey);
  }
  .person-role {
    font-size: 41px;
    font-weight: 400;
    line-height: 48px;
    color: var(--accent-cyan);
  }
  .details {
    list-style: none;
    margin-top: 50px;
  }
  .details li {
    font-size: 35px;
    line-height: 50.5px;
    color: var(--info-grey);
  }
  .details .web { font-style: italic; }
  .details .web span { color: var(--accent-cyan); }
</style>
</head>
<body>
  <div class="card">
    <div class="brand">
      <svg class="brand-dot" width="56" height="56" viewBox="0 0 56 56" aria-hidden="true">
        <circle cx="28" cy="28" r="26" fill="var(--accent-cyan)"/>
      </svg>
      <div class="brand-name">VELUNDA</div>
    </div>

    <div class="divider"></div>

    <div class="contact">
      <h1 class="person-name">Daniel K. Foster</h1>
      <p class="person-role">Chief Manager</p>
      <ul class="details">
        <li class="phone">+20 145 782 903</li>
        <li class="address">2, velunda St., Region 3, 2nd floor</li>
        <li class="email">daniel@velundahealthcare.com</li>
        <li class="web">www.<span>velunda</span>.com</li>
      </ul>
    </div>
  </div>
</body>
</html>
```